two-fold brochure design for oral product

Folded dimension: 21cm*9.5 cm, unfolded dimension: 21*19 cm.
CMYK, 300 pixels, ready for printing.
I hope the brochure would be upmarket.
If you need more elements about our products or brand for this design, pls let me know.

female from 20-40

```html
<!DOCTYPE html>
<html lang="en">
<head>
<meta charset="utf-8">
<title>Gum Essence Brochure – Inner Spread</title>
<link href="https://fonts.googleapis.com/css2?family=Cinzel:wght@700&family=PT+Sans+Narrow:wght@700&family=Roboto+Condensed:wght@300&display=swap" rel="stylesheet">
<style>
  :root{
    --gold:#8a6a1e;
    --gold-light:#c9b27a;
    --green:#5d7a2c;
    --text:#2b2b2b;
    --mint:#a9d6c3;
    --mint-deep:#8cc4ae;
    --frame:#e8dfc4;
    --sage:#b9d3c0;
  }
  *{margin:0;padding:0;box-sizing:border-box}
  html,body{width:1086px;height:1200px;overflow:hidden;background:#fff}
  .spread{position:relative;width:1086px;height:1200px;overflow:hidden;
    background:linear-gradient(180deg,#fff 0,#fff 760px,#e3efe7 900px,#bcd8c6 1200px);
    font-family:"Roboto Condensed",sans-serif;color:var(--text)}
  .botanical-footer{position:absolute;left:0;top:1000px;width:1086px;height:200px;
    background:linear-gradient(180deg,rgba(160,196,170,0) 0,rgba(140,182,150,.55) 100%)}
  .section-title{position:absolute;font-family:"Cinzel",serif;font-weight:700;color:var(--gold);letter-spacing:.5px;line-height:1.05}
  .rule{position:absolute;height:12px;background:linear-gradient(90deg,var(--gold) 0,var(--gold-light) 55%,rgba(255,255,255,0) 100%)}
  .sprig{position:absolute;border-radius:50% 50% 40% 60%;background:radial-gradient(circle at 50% 45%,#b8ceA0 0,#cfdcc0 55%,rgba(255,255,255,0) 72%)}
  .sub{position:absolute;font-family:"PT Sans Narrow",sans-serif;font-weight:700;color:var(--green);font-size:31px;line-height:30px}
  .num{position:absolute;width:21px;height:21px;background:#5a4a1c;color:#fff;font-family:"PT Sans Narrow",sans-serif;font-weight:700;font-size:18px;line-height:21px;text-align:center}
  .bullet{position:absolute;width:11px;height:11px;background:var(--gold-light)}
  .body{position:absolute;font-size:22px;line-height:29px;font-weight:300}
  .body p+p{margin-top:12px}
  .photo{position:absolute;border:7px solid var(--frame);border-radius:60px 0 60px 0;
    background:linear-gradient(160deg,var(--mint) 0,var(--mint-deep) 100%)}
  .photo.face{background:linear-gradient(150deg,#e7c3ad 0,#d59e88 60%,#c0837a 100%)}
  .herbs{position:absolute;left:77px;top:324px;width:417px;height:246px;
    background:radial-gradient(ellipse at 30% 70%,#6e9a4e 0,rgba(110,154,78,.4) 35%,rgba(255,255,255,0) 60%),
               radial-gradient(ellipse at 70% 60%,#a9b97c 0,rgba(220,210,150,.5) 40%,rgba(255,255,255,0) 70%)}
  .ground{position:absolute;left:77px;top:570px;width:417px;height:6px;background:#9fc0a8}
</style>
</head>
<body>
<div class="spread">
  <div class="botanical-footer" role="img" aria-label="Soft botanical illustration of daisies, aloe and herbs along the bottom"></div>

  <!-- Ingredients -->
  <div class="sprig" style="left:4px;top:22px;width:86px;height:126px" role="img" aria-label="Herb sprig ornament"></div>
  <h2 class="section-title" style="left:102px;top:44px;font-size:33px">INGREDIENTS</h2>
  <div class="rule" style="left:0;top:84px;width:500px"></div>
  <div class="rule" style="left:543px;top:82px;width:503px"></div>

  <span class="bullet" style="left:40px;top:176px"></span>
  <h3 class="sub" style="left:78px;top:161px">Actives Components</h3>
  <div class="body" style="left:78px;top:205px;width:420px">
    <p>Acerola extract, Aloe Vera extract, Chamomile extract, Sage extract, Honeysuckle extract, Angelica extract, Coptis extract, Rehmannia Root extract, Echinacea Purpurea extract.</p>
  </div>
  <div class="herbs" role="img" aria-label="Illustration of aloe vera, chamomile, honeysuckle and other medicinal herbs"></div>
  <div class="ground"></div>

  <!-- How to use -->
  <div class="sprig" style="left:2px;top:590px;width:76px;height:120px" role="img" aria-label="Herb sprig ornament"></div>
  <h2 class="section-title" style="left:87px;top:608px;font-size:33px">HOW TO USE</h2>
  <div class="rule" style="left:0;top:648px;width:485px"></div>

  <span class="num" style="left:40px;top:728px">1</span>
  <h3 class="sub" style="left:78px;top:724px">Daily oral care</h3>
  <div class="body" style="left:78px;top:768px;width:222px">
    <p>Brush your teeth with drops on top of toothpaste</p>
    <p>Squeeze the toothpaste onto the toothbrush first, then put a drop of essence on the toothpaste and brush your teeth thoroughly for at least three minutes</p>
  </div>
  <div class="photo" style="left:310px;top:724px;width:198px;height:358px" role="img" aria-label="Photo of a dropper adding essence onto toothpaste on a toothbrush"></div>

  <span class="num" style="left:584px;top:120px">2</span>
  <h3 class="sub" style="left:622px;top:115px;width:200px">Topical oral<br>care</h3>
  <div class="body" style="left:622px;top:188px;width:222px">
    <p>Drop and penetrate between the teeth</p>
    <p>Drop the essence between your teeth or on the uncomfortable area, do not rinse your mouth after dripping, and do not drink water for half an hour.</p>
  </div>
  <div class="photo" style="left:854px;top:116px;width:196px;height:344px" role="img" aria-label="Photo of a dental model with a dropper applying essence between the teeth"></div>

  <span class="num" style="left:584px;top:474px">3</span>
  <h3 class="sub" style="left:622px;top:469px;width:200px">Special oral<br>care</h3>
  <div class="body" style="left:622px;top:540px;width:230px">
    <p>Drop in braces and wear</p>
    <p>Remove the invisible braces or clear retainers, and drip gum essence into the braces to wear.</p>
  </div>
  <div class="photo" style="left:854px;top:482px;width:196px;height:317px" role="img" aria-label="Photo of a dropper over a clear aligner"></div>

  <!-- Protect -->
  <h2 class="section-title" style="left:584px;top:869px;font-size:36px;line-height:42px">PROTECT AND<br>NOURISH</h2>
  <div class="body" style="left:584px;top:960px;width:270px">
    <p>Keep Your Teeth and Gums in Better Conditions.</p>
  </div>
  <div class="photo face" style="left:854px;top:876px;width:196px;height:266px" role="img" aria-label="Close-up photo of a smiling woman's healthy teeth"></div>
</div>
</body>
</html>
```